Business Card Design

I need a business card design for my new solo law practice. I practice consumer bankruptcy law.

I would like a simple, functional business card that looks professional but will also be understandable to regular people - not just other lawyers.
Updates

I added a couple of possible logos that can be incorporated

I'm sorry about the confusion, but the suite number for my new office is suite #150. Thanks for your patience

Target Market(s)

the real target market is potential clients

Industry/Entity Type

Business

Contact Information for Business Card

Law Offices of Theodore M. Vance
Theodore M. Vance
Attorney at Law
Bankruptcy Law
418 Marlowe Court #150
Alder Falls, PA 16842
(555) 317-6482 (Phone)
(555) 317-6497 (Fax)
theov@cedarpointdebtrelief.example
cedarpointdebtrelief.example

Font styles to use
Serif

Requirements
Nice to have
• I've added some possible logos to possible incorporate

```html
<!DOCTYPE html>
<html lang="en">
<head>
<meta charset="utf-8">
<title>Theodore M. Vance – Business Card</title>
<link rel="stylesheet" href="https://fonts.googleapis.com/css2?family=Source+Sans+3:wght@400;600;700&display=swap">
<style>
  :root {
    --backdrop: #3a302c;
    --card-top: #ffffff;
    --card-mid: #eef6de;
    --card-bottom: #8cc63e;
    --navy: #1f3a6e;
    --red: #a3191c;
    --ink: #26406f;
  }
  * { box-sizing: border-box; margin: 0; padding: 0; }
  html, body {
    width: 1200px; height: 564px; overflow: hidden;
    background: var(--backdrop);
    font-family: "Source Sans 3", "Helvetica Neue", Arial, sans-serif;
  }
  .card {
    position: absolute; left: 150px; top: 25px;
    width: 900px; height: 514px;
    background: linear-gradient(175deg, var(--card-top) 0%, var(--card-top) 30%, var(--card-mid) 55%, var(--card-bottom) 100%);
  }
  .brand {
    position: absolute; left: 110px; top: 150px;
    display: flex; align-items: center; gap: 16px;
  }
  .brand-dot {
    width: 46px; height: 46px; border-radius: 50%;
    background: var(--navy);
  }
  .brand-name {
    font-size: 40px; font-weight: 700; color: var(--navy);
  }
  .firm {
    position: absolute; left: 82px; top: 360px;
  }
  .firm-name {
    font-size: 21px; font-weight: 600; color: var(--navy);
    margin-left: 42px;
  }
  .firm-web {
    font-size: 27px; font-weight: 600; color: var(--red);
    margin-top: 2px;
  }
  .identity {
    position: absolute; right: 52px; top: 52px; text-align: right;
  }
  .identity-name {
    font-size: 33px; font-weight: 700; color: var(--red);
    letter-spacing: 0.5px; text-transform: uppercase;
  }
  .identity-title {
    font-size: 19px; font-weight: 700; color: var(--navy);
    margin-top: -2px;
  }
  .contacts {
    position: absolute; right: 52px; top: 175px;
    list-style: none; text-align: right;
    font-size: 18px; color: var(--ink);
  }
  .contacts li {
    display: flex; justify-content: flex-end; align-items: flex-start;
    gap: 14px; margin-bottom: 15px; line-height: 1.3;
  }
  .contacts svg { width: 22px; height: 22px; flex: none; margin-top: 1px; }
  .address { text-align: left; }
</style>
</head>
<body>
  <div class="card">
    <div class="brand">
      <span class="brand-dot"></span>
      <span class="brand-name">Vance Law</span>
    </div>

    <div class="firm">
      <p class="firm-name">Law Offices of Theodore M. Vance</p>
      <p class="firm-web">www.cedarpointdebtrelief.example</p>
    </div>

    <div class="identity">
      <h1 class="identity-name">Theodore M. Vance</h1>
      <p class="identity-title">Attorney at Law Bankruptcy Law</p>
    </div>

    <ul class="contacts">
      <li>(555) 317-6482
        <svg viewBox="0 0 22 22" aria-hidden="true"><rect x="6" y="2" width="11" height="18" rx="2" fill="none" stroke="#1f3a6e" stroke-width="2"/><circle cx="11.5" cy="16.5" r="1" fill="#1f3a6e"/></svg>
      </li>
      <li>(555) 317-6497
        <svg viewBox="0 0 22 22" aria-hidden="true"><rect x="2" y="8" width="18" height="11" rx="2" fill="#1f3a6e"/><rect x="6" y="3" width="10" height="6" fill="none" stroke="#1f3a6e" stroke-width="2"/><rect x="6" y="12" width="10" height="2" fill="#fff"/></svg>
      </li>
      <li>theov@cedarpointdebtrelief.example
        <svg viewBox="0 0 22 22" aria-hidden="true"><rect x="2" y="5" width="18" height="12" fill="#1f3a6e"/><path d="M2 5 L11 12 L20 5" fill="none" stroke="#fff" stroke-width="1.5"/></svg>
      </li>
      <li><span class="address">418 Marlowe Court #150 Alder Falls,<br>PA 16842</span>
        <svg viewBox="0 0 22 22" aria-hidden="true"><path d="M11 2 C6.5 2 4 5.2 4 8.5 C4 13 11 20 11 20 C11 20 18 13 18 8.5 C18 5.2 15.5 2 11 2 Z" fill="#1f3a6e"/><circle cx="11" cy="8.5" r="2.6" fill="#fff"/></svg>
      </li>
    </ul>
  </div>
</body>
</html>
```